Mortgage Broking boutique Business

I’m wanting a revamped look to my existing business card design. I do like the black and silver but happy to have other colours introduced based on your creation. I’ve attached a copy of my current card so you can have a starting point updated details noted brloe. I deal with high net worth individuals so need my card to be sophisticated, classy that gives off a classy vibe

Target Market(s)

High net worth, wealthy

Industry/Entity Type

Mortgage Brokerage

Contact Information for Business Card

Job title: Finance Executive
Phone: +61 7 3287 4419
Mobile: 0471 352 608
Email: marcus@quillbrookcapital.com.au
Web: www.quillbrookcapital.com.au
Address: level 36 Tindale Court, 58 Harwick St Brisbane QLD 4000

Font styles to use
Other font styles liked:
• Helvetica

Colors

Designer to choose colors to be used in the design.

Requirements
Must have
• Use my existing card design as a starting point

```html
<!DOCTYPE html>
<html lang="en">
<head>
<meta charset="utf-8">
<title>Quillbrook Capital – Business Cards</title>
<link rel="stylesheet" href="https://fonts.googleapis.com/css2?family=Cinzel:wght@400;500&family=Raleway:wght@300;400;600&display=swap">
<style>
  :root {
    --page: #ffffff;
    --card: #1d1d1d;
    --card-deep: #151515;
    --silver-light: #f2f2f2;
    --silver-mid: #b5b5b5;
    --silver-dark: #6f6f6f;
    --ink-silver: #d8d8d8;
    --ink-soft: #a9a9a9;
  }
  * { box-sizing: border-box; margin: 0; padding: 0; }
  html, body {
    width: 1200px; height: 1000px; overflow: hidden;
    background: var(--page);
  }
  .canvas { position: relative; width: 1200px; height: 1000px; }

  .card {
    position: absolute;
    width: 340px; height: 200px;
    background: linear-gradient(160deg, var(--card) 0%, var(--card-deep) 100%);
    box-shadow: 4px 6px 10px rgba(0,0,0,0.45);
    color: var(--ink-silver);
    text-align: center;
  }
  .card-frame {
    position: absolute; inset: 8px;
    border: 3px solid transparent;
    border-image: linear-gradient(120deg, var(--silver-dark) 0%, var(--silver-light) 25%, var(--silver-mid) 50%, var(--silver-light) 75%, var(--silver-dark) 100%) 1;
  }
  .card-front .card-frame { border-left-width: 6px; border-right-width: 6px; }

  /* front */
  .brand-mark {
    position: absolute; left: 50%; top: 48px;
    width: 40px; height: 40px; margin-left: -20px;
    border: 2px solid var(--silver-mid);
  }
  .brand-name {
    position: absolute; left: 0; right: 0; top: 134px;
    font-family: "Cinzel", serif; font-weight: 400;
    font-size: 15px; letter-spacing: 3.2px;
    color: var(--ink-silver);
  }

  /* back */
  .brand-small {
    position: absolute; left: 0; right: 0; top: 28px;
    font-family: "Cinzel", serif; font-size: 7px; letter-spacing: 2px;
    color: var(--ink-silver);
  }
  .person-name {
    position: absolute; left: 0; right: 0; top: 72px;
    font-family: "Cinzel", serif; font-size: 21px; letter-spacing: 0.5px;
    color: var(--ink-silver);
  }
  .person-title {
    position: absolute; left: 0; right: 0; top: 99px;
    font-family: "Cinzel", serif; font-size: 12px; letter-spacing: 0.3px;
    color: var(--ink-silver);
  }
  .contact {
    position: absolute; left: 12px; right: 12px; top: 142px;
    font-family: "Raleway", sans-serif; font-weight: 300;
    font-size: 8px; line-height: 16px; color: var(--ink-soft);
    white-space: nowrap;
  }
  .contact b { font-weight: 600; color: var(--ink-silver); }

  .top-front { left: 291px; top: 85px; }
  .top-back  { left: 562px; top: 155px; width: 348px; }
  .lower-back  { left: 452px; top: 572px; }
  .lower-front { left: 480px; top: 705px; }
</style>
</head>
<body>
<main class="canvas">

  <section class="card card-front top-front">
    <div class="card-frame"></div>
    <div class="brand-mark"></div>
    <p class="brand-name">Quillbrook Capital</p>
  </section>

  <section class="card card-back top-back">
    <div class="card-frame"></div>
    <p class="brand-small">Quillbrook Capital</p>
    <h2 class="person-name">Marcus Whitford</h2>
    <p class="person-title">Finance Executive</p>
    <div class="contact">
      <p><b>M:</b> 0471 352 608 <b>| P:</b> +61 7 3287 4419</p>
      <p><b>E:</b> marcus@quillbrookcapital.com.au <b>| W:</b> www.quillbrookcapital.com.au</p>
      <p><b>A:</b> level 36 Tindale Court, 58 Harwick St Brisbane QLD 4000</p>
    </div>
  </section>

  <section class="card card-back lower-back">
    <div class="card-frame"></div>
    <p class="brand-small">Quillbrook Capital</p>
    <h2 class="person-name">Marcus Whitford</h2>
    <p class="person-title">Finance Executive</p>
    <div class="contact">
      <p><b>M:</b> 0471 352 608 <b>| P:</b> +61 7 3287 4419</p>
      <p><b>E:</b> marcus@quillbrookcapital.com.au <b>| W:</b> www.quillbrookcapital.com.au</p>
      <p><b>A:</b> level 36 Tindale Court, 58 Harwick St Brisbane QLD 4000</p>
    </div>
  </section>

  <section class="card card-front lower-front">
    <div class="card-frame"></div>
    <div class="brand-mark"></div>
    <p class="brand-name">Quillbrook Capital</p>
  </section>

</main>
</body>
</html>
```